Tabliq App Analytics Dashboard Design

Our app is designed for visitors centers and hotel/lodging concierges to assist (and allow) travelers to book tours and activities on-site with a kiosk or at front desk. This analytics dashboard will help the hotels or visitors centers owners and employees to understand the activity within their app for their specific business.

We would like this to be modern, clean and sleek and really stand out when we highlight it at an upcoming presentation/conference. The stats we would like to show are:
(By day/month/time period)
Number of Bookings
Source of Bookings i.e. website vs mobile vs kiosk (% of a whole)
Top 5 tour operators booked (and volume of each)
Top 5 tours booked (and volume of each)
Commissions earned (*admin only option - won't show for regular users)

I am including some screen shots of our current Tabliq app to see our general design and color palate. We would like to use this library: https://brambleworks.io/open-source/corvid/gallery

This could lead to further UX design improvements for our current app and future projects. I will be paying out a winner and will provide feedback as the contest goes on.

Target Market(s)

Hotel Concierges & Managers, Visitor Bureau Managers and Employees

Industry/Entity Type

Travel Industry

Other font styles liked:
• Apple Fonts: San Francisco

Requirements
Must have
• We would like to use this library: https://brambleworks.io/open-source/corvid/gallery
• The stats we would like to show are:
• (By day/month/time period)
• Number of Bookings
• Source of Bookings i.e. website vs mobile vs kiosk (% of a whole)
• Top 5 tour operators booked (and volume of each)
• Top 5 tours booked (and volume of each)
• Commissions earned (*admin only option - won't show for regular users)
Nice to have
• Would be nice to have an easy way for users to toggle between time periods that are common and also choose dates from drop down calendars.
• Will be used on an Tabliq and Tabliq Max

```html
<!DOCTYPE html>
<html lang="en">
<head>
<meta charset="utf-8">
<title>Tabliq Dashboard</title>
<link rel="stylesheet" href="https://fonts.googleapis.com/css2?family=Inter:wght@400;500;600;700&display=swap">
<style>
:root{
  --bg:#f2f3f3;
  --sidebar:#121614;
  --green:#10b04f;
  --green-light:#22c55e;
  --text:#1d1f1f;
  --muted:#555;
  --line:#e1e3e3;
  --panel:#ffffff;
  --blue:#1a96e0;
  --orange:#f57d0c;
  --purple:#8e44d6;
  --track:#e2e4e4;
}
*{box-sizing:border-box;margin:0;padding:0}
html,body{width:1200px;height:943px;overflow:hidden;background:var(--bg);font-family:"Inter",sans-serif;color:var(--text)}
.app{position:relative;width:1200px;height:943px}
.sidebar{position:absolute;left:0;top:0;width:113px;height:943px;background:var(--sidebar)}
.status-device{position:absolute;left:8px;top:6px;font-size:11px;color:var(--green-light)}
.nav-item{position:absolute;left:0;width:113px;text-align:center;color:#fff;font-size:12px}
.nav-item svg{display:block;margin:0 auto 8px}
.nav-item.active{color:var(--green-light)}
.nav-item.active::before{content:"";position:absolute;left:0;top:4px;width:3px;height:40px;background:var(--green-light)}
.topbar{position:absolute;left:113px;right:0;top:0;height:80px;background:#fff;border-bottom:1px solid var(--line)}
.status-time{position:absolute;left:0;right:0;top:6px;text-align:center;font-size:11px;color:var(--green)}
.status-battery{position:absolute;right:12px;top:6px;font-size:11px;color:var(--green);display:flex;align-items:center;gap:4px}
.battery{width:24px;height:10px;border:1px solid var(--green);border-radius:2px;padding:1px}
.battery span{display:block;height:100%;background:var(--green)}
.page-title{position:absolute;left:0;right:0;top:40px;text-align:center;font-size:19px;font-weight:600;color:var(--green)}
.segmented{position:absolute;left:129px;top:96px;width:517px;height:34px;display:flex;border:1px solid var(--green);border-radius:3px;overflow:hidden;background:#fff}
.segmented span{flex:1;text-align:center;line-height:32px;font-size:14px;color:var(--green);border-right:1px solid var(--green)}
.segmented span:last-child{border-right:0}
.segmented .on{background:var(--green);color:#fff}
.chart{position:absolute;left:129px;top:146px;width:517px;height:366px;border-radius:4px;overflow:hidden}
.stats{position:absolute;left:667px;top:110px;width:509px;height:90px;display:flex}
.stat{flex:1;text-align:center}
.stat+.stat{border-left:1px solid #ccc}
.stat-value{font-size:36px;font-weight:600;letter-spacing:.5px}
.stat-value sup{font-size:18px;vertical-align:top;position:relative;top:6px}
.stat-label{font-size:12px;color:var(--muted);margin-top:2px}
.panel{position:absolute;background:var(--panel);border-radius:4px;box-shadow:0 1px 3px rgba(0,0,0,.08)}
.panel-title{text-align:center;font-size:18px;font-weight:500;padding:18px 0 14px;margin:0 18px;border-bottom:1px solid var(--line)}
.sources{left:667px;top:228px;width:509px;height:280px}
.donuts{display:flex;justify-content:space-around;padding-top:28px}
.donut{position:relative;width:110px;text-align:center}
.donut-value{position:absolute;left:0;right:0;top:40px;font-size:22px;font-weight:600}
.donut-label{font-size:12px;color:var(--muted);margin-top:8px}
.operators{left:129px;top:540px;width:517px;height:370px}
.tours{left:667px;top:540px;width:509px;height:370px}
.rank-list{list-style:none;padding:10px 18px 0}
.rank-row{display:flex;align-items:center;height:59px}
.thumb{width:46px;height:46px;border-radius:50%;flex:none}
.rank-name{flex:1;font-size:18px;margin-left:12px}
.bar{width:176px;height:10px;border-radius:5px;background:var(--track);overflow:hidden}
.bar span{display:block;height:100%;border-radius:5px}
.operators .bar span{background:var(--blue)}
.tours .bar span{background:var(--orange)}
.pct{width:46px;text-align:right;font-size:13px;font-weight:600}
.operators .pct{color:var(--blue)}
.tours .pct{color:var(--orange)}
</style>
</head>
<body>
<div class="app">
  <aside class="sidebar">
    <div class="status-device">Tabliq</div>
    <div class="nav-item active" style="top:42px">
      <svg width="44" height="44" viewBox="0 0 44 44" fill="none" stroke="#22c55e" stroke-width="2.5"><circle cx="22" cy="22" r="19"/><path d="M22 30 L26 14" stroke-linecap="round"/><circle cx="22" cy="30" r="2" fill="#22c55e"/></svg>
      Dashboard
    </div>
    <div class="nav-item" style="top:155px">
      <svg width="40" height="40" viewBox="0 0 40 40" fill="none" stroke="#fff" stroke-width="2.5"><rect x="4" y="7" width="32" height="29" rx="2"/><path d="M4 14H36M12 3V10M28 3V10"/><g fill="#fff" stroke="none"><rect x="10" y="19" width="4" height="4"/><rect x="18" y="19" width="4" height="4"/><rect x="26" y="19" width="4" height="4"/><rect x="10" y="27" width="4" height="4"/><rect x="18" y="27" width="4" height="4"/><rect x="26" y="27" width="4" height="4"/></g></svg>
      Events
    </div>
    <div class="nav-item" style="top:270px">
      <svg width="40" height="40" viewBox="0 0 40 40" fill="none" stroke="#fff" stroke-width="2.5" stroke-linejoin="round"><path d="M6 10H28V36H10A4 4 0 0 1 6 32Z"/><path d="M28 16H36V32A4 4 0 0 1 28 36"/><path d="M11 18H23M11 24H23M11 30H19"/><path d="M30 4V14M34 4V14"/></svg>
      Bookings
    </div>
    <div class="nav-item" style="top:385px">
      <svg width="40" height="40" viewBox="0 0 40 40" fill="none" stroke="#fff" stroke-width="2.5"><circle cx="20" cy="12" r="8"/><path d="M6 37V30A8 8 0 0 1 14 22H26A8 8 0 0 1 34 30V37Z"/></svg>
      Profile
    </div>
    <div class="nav-item" style="top:500px">
      <svg width="44" height="44" viewBox="0 0 44 44" fill="none" stroke="#fff" stroke-width="2.5" stroke-linejoin="round"><path d="M8 6L14 4L20 16L16 20L4 14Z"/><path d="M18 18L36 36A3 3 0 0 1 32 40L14 22"/><path d="M36 4A8 8 0 0 0 28 14L6 36A3 3 0 0 0 10 40L32 18A8 8 0 0 0 40 8L35 12L32 9Z"/></svg>
      Settings
    </div>
  </aside>

  <header class="topbar">
    <div class="status-time">4:21 PM</div>
    <div class="status-battery">100% <div class="battery"><span></span></div></div>
    <h1 class="page-title">Dashboard</h1>
  </header>

  <div class="segmented"><span>Day</span><span class="on">Month</span><span>Year</span></div>

  <svg class="chart" viewBox="0 0 517 366" font-family="Inter, sans-serif">
    <defs>
      <linearGradient id="chartBg" x1="0" y1="0" x2="0" y2="1"><stop offset="0" stop-color="#0fcf9a"/><stop offset="1" stop-color="#16b04a"/></linearGradient>
      <linearGradient id="areaFill" x1="0" y1="0" x2="0" y2="1"><stop offset="0" stop-color="#e6e41a"/><stop offset="1" stop-color="#6cc52c"/></linearGradient>
    </defs>
    <rect width="517" height="366" fill="url(#chartBg)"/>
    <g stroke="#ffffff" stroke-opacity=".18" stroke-width="1">
      <line x1="40" y1="20" x2="505" y2="20"/><line x1="40" y1="50" x2="505" y2="50"/><line x1="40" y1="80" x2="505" y2="80"/><line x1="40" y1="110" x2="505" y2="110"/><line x1="40" y1="140" x2="505" y2="140"/><line x1="40" y1="170" x2="505" y2="170"/><line x1="40" y1="200" x2="505" y2="200"/><line x1="40" y1="230" x2="505" y2="230"/><line x1="40" y1="260" x2="505" y2="260"/><line x1="40" y1="290" x2="505" y2="290"/>
    </g>
    <g fill="#fff" font-size="12" font-weight="600">
      <text x="4" y="24">1000</text><text x="8" y="54">900</text><text x="8" y="84">800</text><text x="8" y="114">700</text><text x="8" y="144">600</text><text x="8" y="174">500</text><text x="8" y="204">400</text><text x="8" y="234">300</text><text x="8" y="264">200</text><text x="12" y="294">100</text>
    </g>
    <path d="M100 245 C150 236 180 225 215 212 C260 190 290 150 330 134 C370 114 410 100 440 98 L440 320 L100 320 Z" fill="url(#areaFill)"/>
    <path d="M100 245 C150 236 180 225 215 212 C260 190 290 150 330 134 C370 114 410 100 440 98" fill="none" stroke="#f2ec3a" stroke-width="1.5"/>
    <g fill="#7dcf34" stroke="#fff" stroke-width="2"><circle cx="100" cy="245" r="6"/><circle cx="215" cy="212" r="6"/><circle cx="330" cy="134" r="6"/><circle cx="440" cy="98" r="6"/></g>
    <g fill="#fff" font-size="14" text-anchor="middle"><text x="100" y="350">5 Jun</text><text x="215" y="350">12 Jun</text><text x="330" y="350">19 Jun</text><text x="440" y="350">26 Jun</text></g>
    <g fill="none" stroke="#fff" stroke-width="1.8" stroke-linecap="round" stroke-linejoin="round">
      <circle cx="24" cy="345" r="11"/><path d="M29 345H19M23 341L19 345L23 349"/>
      <circle cx="496" cy="343" r="11"/><path d="M491 343H501M497 339L501 343L497 347"/>
    </g>
  </svg>

  <section class="stats">
    <div class="stat"><div class="stat-value">728</div><div class="stat-label">NO. OF BOOKINGS</div></div>
    <div class="stat"><div class="stat-value"><sup>$</sup>290</div><div class="stat-label">COMMISSIONS RECEIVED</div></div>
  </section>

  <section class="panel sources">
    <h2 class="panel-title">SOURCE OF BOOKINGS</h2>
    <div class="donuts">
      <div class="donut">
        <svg width="110" height="110" viewBox="0 0 110 110"><circle cx="55" cy="55" r="47" fill="none" stroke="var(--track)" stroke-width="11"/><circle cx="55" cy="55" r="47" fill="none" stroke="var(--orange)" stroke-width="11" stroke-dasharray="88.6 206.7" transform="rotate(-90 55 55)"/></svg>
        <div class="donut-value">30%</div><div class="donut-label">WEBSITE</div>
      </div>
      <div class="donut">
        <svg width="110" height="110" viewBox="0 0 110 110"><circle cx="55" cy="55" r="47" fill="none" stroke="var(--track)" stroke-width="11"/><circle cx="55" cy="55" r="47" fill="none" stroke="var(--blue)" stroke-width="11" stroke-dasharray="147.7 147.6" transform="rotate(-90 55 55)"/></svg>
        <div class="donut-value">50%</div><div class="donut-label">MOBILE</div>
      </div>
      <div class="donut">
        <svg width="110" height="110" viewBox="0 0 110 110"><circle cx="55" cy="55" r="47" fill="none" stroke="var(--track)" stroke-width="11"/><circle cx="55" cy="55" r="47" fill="none" stroke="var(--purple)" stroke-width="11" stroke-dasharray="59 236.3" transform="rotate(-90 55 55)"/></svg>
        <div class="donut-value">20%</div><div class="donut-label">KIOSK</div>
      </div>
    </div>
  </section>

  <section class="panel operators">
    <h2 class="panel-title">TOP 5 TOUR OPERATORS BOOKED</h2>
    <ul class="rank-list">
      <li class="rank-row"><div class="thumb" role="img" aria-label="Operator portrait" style="background:linear-gradient(#a9c4dc,#7b8f9c)"></div><span class="rank-name">Dorian Kessel</span><div class="bar"><span style="width:92%"></span></div><span class="pct">92%</span></li>
      <li class="rank-row"><div class="thumb" role="img" aria-label="Operator portrait" style="background:linear-gradient(#6c7379,#2f3438)"></div><span class="rank-name">Marlow Benning</span><div class="bar"><span style="width:86%"></span></div><span class="pct">86%</span></li>
      <li class="rank-row"><div class="thumb" role="img" aria-label="Operator portrait" style="background:linear-gradient(#5a5350,#2a2624)"></div><span class="rank-name">Tobias Renfield</span><div class="bar"><span style="width:74%"></span></div><span class="pct">74%</span></li>
      <li class="rank-row"><div class="thumb" role="img" aria-label="Operator portrait" style="background:linear-gradient(#8a9a80,#3d4a3c)"></div><span class="rank-name">Callum Ashgrove</span><div class="bar"><span style="width:68%"></span></div><span class="pct">68%</span></li>
      <li class="rank-row"><div class="thumb" role="img" aria-label="Operator portrait" style="background:linear-gradient(#e7d4c8,#b23a3a)"></div><span class="rank-name">Elias Varnham</span><div class="bar"><span style="width:60%"></span></div><span class="pct">60%</span></li>
    </ul>
  </section>

  <section class="panel tours">
    <h2 class="panel-title">TOP 5 TOURS BOOKED</h2>
    <ul class="rank-list">
      <li class="rank-row"><div class="thumb" role="img" aria-label="Theme park photo" style="background:linear-gradient(#9db6d0,#a0523a)"></div><span class="rank-name">Lumen Gardens</span><div class="bar"><span style="width:92%"></span></div><span class="pct">92%</span></li>
      <li class="rank-row"><div class="thumb" role="img" aria-label="River scenery photo" style="background:linear-gradient(#1f6b3a,#0c3a22)"></div><span class="rank-name">Silverbend River</span><div class="bar"><span style="width:86%"></span></div><span class="pct">86%</span></li>
      <li class="rank-row"><div class="thumb" role="img" aria-label="Aquarium photo" style="background:linear-gradient(#7fb3e0,#2d6fb0)"></div><span class="rank-name">Coral Bay Aquarium</span><div class="bar"><span style="width:74%"></span></div><span class="pct">74%</span></li>
      <li class="rank-row"><div class="thumb" role="img" aria-label="Adventure park photo" style="background:linear-gradient(#8ea07a,#6a4a32)"></div><span class="rank-name">Ridgeway Adventure Park</span><div class="bar"><span style="width:68%"></span></div><span class="pct">68%</span></li>
      <li class="rank-row"><div class="thumb" role="img" aria-label="Hilltop resort photo" style="background:linear-gradient(#cfe3ef,#3d8fb8)"></div><span class="rank-name">Skyreach Heights</span><div class="bar"><span style="width:60%"></span></div><span class="pct">60%</span></li>
    </ul>
  </section>
</div>
</body>
</html>
```